Verdant Pathworks Business Card

want the back of card to be blue- with the logo in the center
front of card- info plus logo (info being mailing address, email address, and website address )
4 different names with titles to have on cards
1) Dominic Ashvale - Owner
2) Bethany Korvuth- Customer Relationship Specialist
3) Luca Brennwick- Vice President of Sales
4) Neil Umbright- Chief Technology Officer

Target Market(s)

tech company in the government/probation office industry

Industry/Entity Type

Government Office

Contact Information for Business Card

1) Dominic Ashvale - Owner

Colors
0355a3
ffffff

Requirements
Must have
• back side should be blue, with the logo placed in the center
• front side needs to include both the logo, as well as company info (info should include website address, email address, and mailing address)

```html
<!DOCTYPE html>
<html lang="en">
<head>
<meta charset="utf-8">
<title>Verdant Pathworks Business Card</title>
<link rel="stylesheet" href="https://fonts.googleapis.com/css2?family=Lato:wght@400;700&display=swap">
<style>
  :root {
    --brand-blue: #0355a3;
    --card-white: #ffffff;
    --text-grey: #7a7a7a;
    --rule-grey: #b5b5b5;
    --page-bg: #e9e7e3;
  }
  * { margin: 0; padding: 0; box-sizing: border-box; }
  html, body { width: 900px; height: 1200px; overflow: hidden; }
  body {
    background: var(--page-bg);
    font-family: "Lato", sans-serif;
    position: relative;
  }
  .card {
    position: absolute;
    left: 87px;
    width: 733px;
    height: 429px;
    border-radius: 28px;
  }
  .card-front { top: 137px; background: var(--card-white); }
  .card-back { top: 633px; background: var(--brand-blue); }

  .brand-block {
    position: absolute;
    left: 50px;
    top: 150px;
    width: 270px;
    text-align: center;
    color: var(--brand-blue);
  }
  .brand-square {
    display: block;
    width: 44px;
    height: 44px;
    margin: 0 auto 14px;
    background: var(--brand-blue);
  }
  .brand-name {
    font-weight: 700;
    font-size: 36px;
    line-height: 1.05;
    letter-spacing: 1px;
  }

  .divider {
    position: absolute;
    left: 382px;
    top: 127px;
    width: 2px;
    height: 192px;
    background: var(--rule-grey);
  }

  .contact {
    position: absolute;
    left: 405px;
    top: 116px;
    color: var(--text-grey);
    font-size: 17px;
    letter-spacing: 0.4px;
  }
  .person-name {
    color: var(--brand-blue);
    font-size: 34px;
    font-weight: 400;
    line-height: 1.1;
  }
  .person-title { margin-top: 2px; line-height: 1.3; }
  .address { margin-top: 11px; line-height: 25px; }
  .contact-lines { margin-top: 6px; list-style: none; }
  .contact-lines li {
    display: flex;
    align-items: center;
    height: 27px;
  }
  .contact-lines svg {
    width: 14px;
    height: 14px;
    margin-right: 10px;
    fill: var(--brand-blue);
    flex: none;
  }

  .back-brand {
    position: absolute;
    left: 50%;
    top: 50%;
    transform: translate(-50%, -50%);
    width: 240px;
    text-align: center;
    color: var(--card-white);
  }
  .back-brand .brand-square {
    width: 44px;
    height: 44px;
    background: var(--card-white);
    margin-bottom: 14px;
  }
</style>
</head>
<body>
  <section class="card card-front">
    <div class="brand-block">
      <span class="brand-square"></span>
      <div class="brand-name">Verdant<br>Pathworks</div>
    </div>
    <div class="divider"></div>
    <div class="contact">
      <h1 class="person-name">Dominic Ashvale</h1>
      <p class="person-title">Owner</p>
      <p class="address">48 Harrow Lane, Suite B<br>London, UK 204517</p>
      <ul class="contact-lines">
        <li>
          <svg viewBox="0 0 24 24" aria-hidden="true"><path d="M6.6 10.8a15.1 15.1 0 0 0 6.6 6.6l2.2-2.2a1 1 0 0 1 1-.25 11.4 11.4 0 0 0 3.6.57 1 1 0 0 1 1 1V20a1 1 0 0 1-1 1A17 17 0 0 1 3 4a1 1 0 0 1 1-1h3.5a1 1 0 0 1 1 1c0 1.25.2 2.45.57 3.57a1 1 0 0 1-.25 1z"/></svg>
          000 000 0000
        </li>
        <li>
          <svg viewBox="0 0 24 24" aria-hidden="true"><path d="M2 5h20v2l-10 6L2 7z"/><path d="M2 9l10 6 10-6v10H2z"/></svg>
          dominic@verdantpathworks.com
        </li>
        <li>
          <svg viewBox="0 0 24 24" aria-hidden="true"><path fill-rule="evenodd" d="M12 2a10 10 0 1 1 0 20 10 10 0 0 1 0-20zm-1.1 2.1A8 8 0 0 0 4.1 11h3.4c.1-2.6.8-5 2-6.9h1.4zm2.2 0h1.4c1.2 1.9 1.9 4.3 2 6.9h3.4a8 8 0 0 0-6.8-6.9zM12 4.4c-1.3 1.7-2.2 4-2.4 6.6h4.8c-.2-2.6-1.1-4.9-2.4-6.6zM4.1 13a8 8 0 0 0 6.8 6.9H9.5c-1.2-1.9-1.9-4.3-2-6.9zm5.5 0c.2 2.6 1.1 4.9 2.4 6.6 1.3-1.7 2.2-4 2.4-6.6zm6.9 0c-.1 2.6-.8 5-2 6.9h-1.4a8 8 0 0 0 6.8-6.9z"/></svg>
          www.verdantpathworks.com
        </li>
      </ul>
    </div>
  </section>

  <section class="card card-back">
    <div class="back-brand">
      <span class="brand-square"></span>
      <div class="brand-name">Verdant<br>Pathworks</div>
    </div>
  </section>
</body>
</html>
```